Lowmoor Guild - Crossroads CD Cover

To prepare a CD Cover for the single "Crossroads" by Lowmoor Guild.
You can hear the single here:
http://lowmoorguild.com/listen/

The LMG logo and backdrop are also provided if you want to incorporate them into the CD cover design, though that isn't mandatory.

Song is about deciding on taking on a serious relationship, and leaving the single life behind.

Target Market(s)

Music listeners, 18-50 yrs old, into retro 80s, Marigolds/Dune Riders

Industry/Entity Type

Music Download

Requirements
Must have
• LMG logo
• Crossroads title
Nice to have
• Use of backdrop, or facimile
Should not have
• Too obvious on the term Crossroads

```html
<!DOCTYPE html>
<html lang="en">
<head>
<meta charset="utf-8">
<title>Lowmoor Guild – Crossroads</title>
<link rel="stylesheet" href="https://fonts.googleapis.com/css2?family=Antonio:wght@300&family=Sacramento&display=swap">
<style>
  :root {
    --page-bg: #22252f;
    --cover-deep: #08090d;
    --cover-night: #121830;
    --cover-indigo: #1c2358;
    --title-copper: #c38d5e;
    --logo-white: #f4f4f2;
  }
  html, body {
    margin: 0;
    padding: 0;
    width: 1200px;
    height: 1114px;
    overflow: hidden;
    background: var(--page-bg);
  }
  .canvas {
    position: relative;
    width: 1200px;
    height: 1114px;
    background: var(--page-bg);
  }
  .cover {
    position: absolute;
    left: 134px;
    top: 96px;
    width: 936px;
    height: 900px;
    overflow: hidden;
  }
  .cover-art {
    position: absolute;
    inset: 0;
    background:
      radial-gradient(ellipse 45% 20% at 55% 4%, var(--cover-indigo) 0%, transparent 100%),
      radial-gradient(ellipse 50% 35% at 30% 60%, var(--cover-night) 0%, transparent 100%),
      radial-gradient(ellipse 40% 35% at 85% 35%, var(--cover-night) 0%, transparent 100%),
      var(--cover-deep);
  }
  .title-line {
    position: absolute;
    left: 0;
    right: 0;
    top: 457px;
    height: 1px;
    background: var(--title-copper);
    opacity: 0.85;
  }
  .title {
    position: absolute;
    left: 0;
    right: 0;
    top: 412px;
    margin: 0;
    text-align: center;
    font-family: "Sacramento", cursive;
    font-weight: 400;
    font-size: 54px;
    line-height: 60px;
    letter-spacing: 52px;
    padding-left: 52px;
    color: var(--title-copper);
    text-transform: lowercase;
  }
  .logo {
    position: absolute;
    right: 40px;
    top: 790px;
    margin: 0;
    font-family: "Antonio", sans-serif;
    font-weight: 300;
    font-size: 50px;
    line-height: 50px;
    color: var(--logo-white);
    text-transform: uppercase;
    text-align: left;
  }
  .logo span { display: block; }
</style>
</head>
<body>
  <main class="canvas">
    <section class="cover">
      <div class="cover-art" role="img" aria-label="Starry night sky scattered with hand-painted rings in copper, red and green"></div>
      <div class="title-line"></div>
      <h1 class="title">crossroads</h1>
      <p class="logo"><span>Lowmoor</span><span>Guild</span></p>
    </section>
  </main>
</body>
</html>
```